Dog treat Package Design

We’re looking for a creative and professional designer to develop eye-catching packaging for our upcoming line of premium dog treats under the Tailor Munch brand.
The design should reflect quality, trust, and natural nutrition, appealing to dog owners who value healthy, high-end pet products.
What We Need
Full packaging design for a resealable stand-up pouch (approx. 130 × 210 + 60 mm)
Front and back layout including space for logo, product name, ingredients, nutrition panel, barcode, and storage instructions
Print-ready files (with dielines, bleeds, and crop marks)
Editable source file (AI / PSD preferred)
3D mock-up or realistic rendering for presentation
Design Direction
Clean, minimal, and modern look with a premium feel
Use natural tones (e.g. earthy browns, creams, muted greens, or soft neutrals)
Should convey trust, wellness, and craftsmanship
Incorporate subtle texture or illustration that hints at natural ingredients or happy, healthy dogs
Must be consistent across potential product variations (e.g. chicken, beef, lamb treats)
Target Audience
Pet owners who value nutrition, quality ingredients, and design aesthetics — typically aged 25–50, with a focus on healthy, Australian-made pet products.
Deliverables
2 initial design concepts
Up to 2 revision rounds
Final deliverables in:
Print-ready PDF (CMYK)
Editable AI/PSD
High-resolution mock-ups
Design style similar to Fennel Paws
Target Market(s)
People with pets - Premium
Look and feel
Each slider illustrates characteristics of the customer's brand and the style your logo design should communicate.

```html
<!DOCTYPE html>
<html lang="en">
<head>
<meta charset="utf-8">
<title>Tailor Munch Chicken Treats Pouch</title>
<link rel="stylesheet" href="https://fonts.googleapis.com/css2?family=Montserrat:wght@400;600;700;800&display=swap">
<style>
  :root {
    --bg: #dcdcdc;
    --cream: #e2ddcf;
    --cream-light: #e9e5d9;
    --brown: #3d3530;
    --green: #a9c77e;
    --orange: #e8883a;
    --white: #ffffff;
    --meat-1: #b8442a;
    --meat-2: #d96a3c;
  }
  * { box-sizing: border-box; margin: 0; padding: 0; }
  html, body { width: 1200px; height: 1200px; overflow: hidden; }
  body {
    background: var(--bg);
    font-family: "Montserrat", sans-serif;
    color: var(--brown);
    position: relative;
  }
  .pouch {
    position: absolute;
    left: 330px; top: 160px;
    width: 540px; height: 880px;
    border-radius: 10px;
    overflow: hidden;
    background: var(--cream);
  }
  .pouch > * { position: absolute; }
  .banner { left: 40px; top: 24px; width: 460px; height: 46px; }
  .banner-text {
    left: 40px; top: 24px; width: 460px; height: 46px;
    display: flex; align-items: center; justify-content: center;
    font-weight: 800; font-size: 19px; letter-spacing: 1.5px; color: var(--cream-light);
  }
  .seal-line { left: 40px; width: 460px; height: 2px; background: #d3cdbd; }
  .botanical { width: 120px; height: 270px; top: 115px;
    background: linear-gradient(180deg, rgba(184,180,166,0.35), rgba(184,180,166,0.12)); border-radius: 60px; }
  .botanical.left { left: 6px; }
  .botanical.right { right: 6px; }
  .brand {
    left: 0; width: 540px; top: 228px;
    display: flex; align-items: center; justify-content: center; gap: 12px;
  }
  .brand-dot { width: 14px; height: 14px; border-radius: 50%; background: var(--brown); }
  .brand-name { font-weight: 600; font-size: 24px; color: var(--brown); }
  .tagline { left: 0; width: 540px; top: 270px; text-align: center;
    font-weight: 400; font-size: 12px; }
  .lower { left: 0; top: 370px; width: 540px; height: 510px; background: var(--green); }
  .grass { left: 0; top: 345px; width: 540px; height: 30px;
    background: linear-gradient(180deg, rgba(169,199,126,0), var(--green)); }
  .stat-tab { left: 51px; top: 411px; width: 92px; height: 187px;
    background: var(--orange); border-radius: 46px 46px 0 0; color: var(--white); }
  .stat-icon { position: absolute; left: 21px; top: 18px; width: 50px; height: 58px;
    background: rgba(255,255,255,0.85); border-radius: 24px 24px 6px 6px; }
  .stat { position: absolute; left: 12px; }
  .stat small { display: block; font-size: 11px; font-weight: 400; }
  .stat strong { display: block; font-size: 24px; font-weight: 800; line-height: 1; }
  .stat.protein { top: 90px; }
  .stat.fat { top: 138px; }
  .stat-rule { position: absolute; left: 10px; width: 72px; top: 133px; height: 1px; background: var(--white); }
  .product-name { left: 155px; top: 455px; font-weight: 800; font-size: 37px; letter-spacing: 0.5px; }
  .claims { left: 205px; top: 508px; display: flex; gap: 22px; }
  .claim { width: 70px; text-align: center; font-size: 11px; font-weight: 700; line-height: 1.1; }
  .claim svg { display: block; margin: 0 auto 4px; }
  .window { left: 42px; top: 598px; width: 460px; height: 208px;
    background: linear-gradient(100deg, var(--meat-1), var(--meat-2) 35%, var(--meat-1) 60%, var(--meat-2) 85%, var(--meat-1)); }
  .footer-note { top: 818px; font-weight: 700; font-size: 13px; }
  .footer-note.left { left: 54px; }
  .footer-note.right { right: 70px; }
</style>
</head>
<body>
<main class="pouch">
  <svg class="banner" viewBox="0 0 460 46" aria-hidden="true">
    <circle cx="16" cy="13" r="13" fill="#3d3530"/><circle cx="16" cy="33" r="13" fill="#3d3530"/>
    <circle cx="444" cy="13" r="13" fill="#3d3530"/><circle cx="444" cy="33" r="13" fill="#3d3530"/>
    <rect x="14" y="4" width="432" height="38" rx="6" fill="#3d3530"/>
  </svg>
  <div class="banner-text">FOR HAPPY HEALTHY DOGS!</div>
  <div class="seal-line" style="top:92px"></div>
  <div class="seal-line" style="top:100px"></div>

  <div class="botanical left" role="img" aria-label="Line illustration of leafy herb sprigs"></div>
  <div class="botanical right" role="img" aria-label="Line illustration of leafy herb sprigs"></div>

  <div class="brand">
    <span class="brand-dot" aria-hidden="true"></span>
    <span class="brand-name">Tailor Munch</span>
  </div>
  <div class="tagline">Real Food. Real Joy</div>

  <div class="lower"></div>
  <div class="grass" role="img" aria-label="Illustrated green grass edge"></div>

  <div class="stat-tab">
    <div class="stat-icon" role="img" aria-label="Chicken illustration"></div>
    <div class="stat protein"><small>Protein</small><strong>26%</strong></div>
    <div class="stat-rule"></div>
    <div class="stat fat"><small>Fat</small><strong>12%</strong></div>
  </div>

  <h1 class="product-name">CHICKEN TREATS</h1>

  <div class="claims">
    <div class="claim">
      <svg width="60" height="60" viewBox="0 0 60 60"><circle cx="30" cy="30" r="27" fill="none" stroke="#3d3530" stroke-width="3"/><circle cx="30" cy="26" r="7" fill="none" stroke="#3d3530" stroke-width="2.5"/><path d="M14 40 H46 M18 45 H42" stroke="#3d3530" stroke-width="2.5"/></svg>
      Free<br>Range
    </div>
    <div class="claim">
      <svg width="60" height="60" viewBox="0 0 60 60"><circle cx="30" cy="30" r="27" fill="none" stroke="#3d3530" stroke-width="3"/><path d="M30 14 V46" stroke="#3d3530" stroke-width="3"/><path d="M11 11 L49 49" stroke="#3d3530" stroke-width="3"/></svg>
      Grain<br>Free
    </div>
    <div class="claim">
      <svg width="60" height="60" viewBox="0 0 60 60"><circle cx="30" cy="30" r="27" fill="none" stroke="#3d3530" stroke-width="3"/><path d="M26 16 V28 L19 42 H41 L34 28 V16" fill="none" stroke="#3d3530" stroke-width="2.5"/><path d="M11 11 L49 49" stroke="#3d3530" stroke-width="3"/></svg>
      No<br>Preservatives
    </div>
  </div>

  <div class="window" role="img" aria-label="Clear window showing dried chicken jerky strips"></div>

  <p class="footer-note left">PET FOOD ONLY</p>
  <p class="footer-note right">120g NET</p>
</main>
</body>
</html>
```